依頼詳細
****************************
全国各地で少年詩を創作している詩人たちの応募作品の中から、「子どもにもわかる言葉で書かれた文学性の高い詩作品」を選定し発表しているアンソロジーです。
1984年から年刊「明日童謡選」として20年刊継続してまいりました。2004年より「こどもとひらく童心詩選」と改題し、新たな体制で少年詩のより一層の普及と質的向上をめざしています。

参加費:掲載された場合には予価2,400円(税別)の本を5冊以上ご購入いただきます。(割引あり)(別途送料)*別紙の規約など参照。

選定は任期3年で7名の編集委員により実施されております。
現在の編集委員は
杉浦航一郎(詩人・絵本作家)
くらもと・さよこ(詩人)
島田 薫(小説家・緑陵大学教授)
●●●●(詩人)*未確定なので、一旦この記載
●●●●(詩人)*未確定なので、一旦この記載
岡部里香子(青い窓舎 代表取締役)
森川静江(青い窓舎 編集長)

以上7名です。
編集委員により掲載・不掲載が決定しますが、各編集委員には「5点」を持ち点として、校正刷りの段階で優秀な作品に点数を振り分けてもらい、最優秀作品を決定しております。
最優秀賞に賞金などは出ませんが、粗品を贈呈しております。

なお、学校に協力してもらい、校正刷りの段階にて授業などで活用し、子どもたちの感想を直接もらう取り組みをしております。また実際に詩人を授業に招待する活動もしています。
子どもたちには「好きな作品3つ選んで」とお願いをしてコメントをもらっています。
編集委員、子どもたちの集計結果とコメントは刊行される『こどもとひらく童心詩選』に挟み込まれる「ことのは便り」にて紹介させていただいております。集まった子どもの感想は詩人たちにフィードバックしております。(毎年約400名以上の生徒が参加。)

刊行後は主に公共図書館や学校図書館に納品されます。もちろん全国の書店やBookvaleなどでも購入可能です。
*******************************

主に郵送でご案内をします。
全国各地で詩を書いている人、約2,000人にDMする予定です。
DMの一番トップに、今回のチラシを添えたいと考えております。
同封物として、規定や確認書なども同封します。
が、規約などの細かな部分は読まないので、パッと見ただけで「あ〜、子どもたちを読書対象とした作品の募集をしているんだな。」が理解できると嬉しいです。

他者にない特徴としては、上記にもある《校正刷りの段階で学校と協力して授業でも活用している》ことだと感じています。

作品応募・掲載→編集委員・生徒の感想フィードバック→次年度に質的向上した詩作品の応募・・・このサイクルを目指しています。
生徒にとってもテストの点数に関係がない「詩を味わう時間」という贅沢な時間を経験し、言葉の引き出しを増やしてもらっています。

主に郵送でご案内をします。
全国各地で物語を書いている人、約2,000人にDMする予定です。
同封物として、規定や確認書なども同封します。
が、規約などの細かな部分は読まないですし、パッと見ただけで「あ〜、子どもたちを読書対象とした作品の募集をしているんだな。」が理解できると嬉しいです。

投稿は専用の原稿用紙のみ受け付けとなっているので、弊社に問い合わせ(投稿規定や原稿用紙)をいただけるようにしていただけると幸いです。
記載項目
社名、書名、編集委員、締め切り、問い合わせ先など
サイズ
A4
ページ数
片面
希望イメージ
シンプル 複雑
単色 カラフル
暗い 明るい
日常 高級
遊び心 厳粛
未来的 伝統的
女性的 男性的
希望する色
設定なし
納品ファイル
• イラストレーター形式 (.ai)
• フォトショップ形式 (.psd)
補足説明
*今回より編集委員が変更になっております。
*チラシは昨年のワークリンク採用作品です。
■ 選んだ理由

応募内容などの文字が読みやすいこと。
締め切りの3月末の春を迎える寸前の雰囲気を感じること。
などから選ばせていただきました。

■ 提案者全員のお礼・コメント

この度も素敵なご提案をありがとうございました!
票が全て割れるような事態になるくらい、最終的には好みの段階で選考させていただくような結果となりました。
今後ともよろしくお願いします。

```html
<!DOCTYPE html>
<html lang="ja">
<head>
<meta charset="utf-8">
<title>こどもとひらく童心詩選2019 作品募集</title>
<link href="https://fonts.googleapis.com/css2?family=Zen+Old+Mincho:wght@500;700;900&family=Noto+Sans+JP:wght@400;500;700&display=swap" rel="stylesheet">
<style>
  :root{
    --blue:#2f74b5;
    --blue-deep:#1f5a95;
    --blue-pale:#e4f0f9;
    --ink:#333;
    --ink-soft:#555;
    --paper:#fffdf8;
    --line:#9cc3e3;
    --sky-a:#f6f9fc;
    --sky-b:#fbf4ea;
    --sky-c:#eef4ea;
  }
  *{box-sizing:border-box;margin:0;padding:0}
  html,body{width:849px;height:1200px;overflow:hidden;background:#fff}
  body{font-family:"Noto Sans JP",sans-serif;color:var(--ink)}
  .flyer{position:relative;width:849px;height:1200px;background:var(--paper);overflow:hidden}

  .hero-art{position:absolute;left:0;top:0;width:849px;height:420px;
    background:linear-gradient(160deg,var(--sky-a) 0%,var(--sky-b) 55%,var(--sky-c) 100%)}

  .lead{position:absolute;top:22px;right:118px;writing-mode:vertical-rl;
    font-family:"Zen Old Mincho",serif;font-weight:700;font-size:18px;letter-spacing:1px;color:var(--ink-soft)}
  .headline{position:absolute;top:44px;right:52px;writing-mode:vertical-rl;
    font-family:"Zen Old Mincho",serif;font-weight:900;font-size:38px;line-height:1;color:var(--blue)}

  .title-block{position:absolute;top:424px;left:0;width:849px;text-align:center}
  .title-kicker{font-family:"Zen Old Mincho",serif;font-weight:700;font-size:19px;color:var(--ink-soft);letter-spacing:2px}
  .title{margin-top:4px;font-family:"Zen Old Mincho",serif;font-weight:900;color:var(--blue);line-height:1.1}
  .title .pre{font-size:30px}
  .title .main{font-size:50px}

  .deadline{position:absolute;top:532px;left:160px;width:529px;height:40px;
    border-top:1px solid var(--line);border-bottom:1px solid var(--line);
    display:flex;align-items:center;justify-content:center;gap:8px;color:var(--blue-deep)}
  .deadline .label{font-size:15px;font-weight:500}
  .deadline .date{font-size:23px;font-weight:700;letter-spacing:1px}

  .body{position:absolute;top:588px;left:36px;width:777px;height:590px;
    border:1.5px solid var(--line);border-radius:10px;background:#fff}

  .info{position:absolute;top:24px;left:24px;width:488px;font-size:12.4px;line-height:1.72;color:var(--ink)}
  .info h2{font-size:15px;font-weight:700;color:var(--blue-deep);margin:14px 0 6px;
    padding-bottom:3px;border-bottom:1px dashed var(--line)}
  .info h2:first-child{margin-top:0}
  .info p{text-indent:1em}
  .info ul{list-style:none}
  .info li{padding-left:1.1em;text-indent:-1.1em;margin-bottom:5px}
  .info li::before{content:"●";color:var(--blue);margin-right:2px}
  .info strong{color:var(--blue-deep)}

  .editors{position:absolute;top:24px;right:22px;width:228px;border:1.5px solid var(--blue);border-radius:6px;overflow:hidden}
  .editors h3{background:var(--blue);color:#fff;font-size:15px;font-weight:700;text-align:center;padding:5px 0;letter-spacing:4px}
  .editors ul{list-style:none;padding:10px 12px 8px;background:var(--blue-pale)}
  .editors li{font-size:13px;line-height:1.45;margin-bottom:6px}
  .editors .name{font-weight:700}
  .editors .role{display:block;font-size:11px;color:var(--ink-soft)}

  .publisher{position:absolute;right:22px;bottom:54px;width:228px;font-size:11.5px;line-height:1.6;color:var(--ink-soft)}
  .publisher .tagline{font-size:11px;letter-spacing:1px}
  .brand{display:flex;align-items:center;gap:8px;margin:2px 0 8px}
  .brand .dot{width:16px;height:16px;border-radius:50%;background:var(--blue)}
  .brand .name{font-size:26px;font-weight:700;color:var(--blue-deep);letter-spacing:2px}
  .contact-row{display:flex;align-items:center;gap:5px;font-size:14px;font-weight:700;color:var(--ink)}
  .contact-row svg{width:14px;height:14px}

  .request{position:absolute;left:24px;bottom:16px;width:488px;border:1px solid var(--blue);
    padding:5px 10px;font-size:11.5px;color:var(--blue-deep);background:var(--blue-pale)}
</style>
</head>
<body>
<main class="flyer">
  <div class="hero-art" role="img" aria-label="パステル調の水彩イラスト：本を読む少女と小さなリス、鳥、虹、ふわりと浮かぶ『ぽえむ』の文字"></div>

  <p class="lead">子どもにもわかる言葉で書かれた文学性の高い</p>
  <h1 class="headline">詩作品を募集します。</h1>

  <header class="title-block">
    <p class="title-kicker">学校の授業でも活用する</p>
    <p class="title"><span class="pre">こどもとひらく</span><span class="main">童心詩選2019</span></p>
  </header>

  <div class="deadline">
    <span class="label">応募締め切り：</span>
    <span class="date">2019年３月末日必着</span>
  </div>

  <section class="body">
    <div class="info">
      <h2>■ 趣旨</h2>
      <p>『こどもとひらく童心詩選』は、全国各地で少年詩を創作している詩人たちの応募作品の中から、子どもにもわかる言葉で書かれた文学性の高い詩作品を選定し発表しているアンソロジーです。1984年創刊、年刊『明日童謡選』として20年刊継続し、2004年より『こどもとひらく童心詩選』と改題。少年詩のより一層の普及と質的向上をめざしています。</p>

      <h2>■ 募集にあたって</h2>
      <ul>
        <li><strong>特徴：</strong>学校の協力を得て、校正刷りの段階から授業で活用。子どもたちが「好きな作品3つ」を選び、感想を寄せます。集計結果とコメントは「ことのは便り」でご紹介し、詩人へフィードバックします。</li>
        <li><strong>選考：</strong>任期3年・7名の編集委員が掲載を決定。各委員の持ち点により最優秀作品を選び、粗品を贈呈します。</li>
        <li><strong>参加費：</strong>掲載の場合、予価2,400円（税別）の本を5冊以上ご購入いただきます。（割引あり・別途送料）</li>
        <li><strong>刊行後：</strong>主に公共図書館・学校図書館に納品。全国の書店やBookvaleでもお求めいただけます。</li>
        <li><strong>投稿方法：</strong>専用の原稿用紙のみ受け付けます。投稿規定・原稿用紙は下記までお問い合わせください。</li>
      </ul>
    </div>

    <aside class="editors">
      <h3>編集委員</h3>
      <ul>
        <li><span class="name">杉浦航一郎</span><span class="role">（詩人・絵本作家）</span></li>
        <li><span class="name">くらもと・さよこ</span><span class="role">（詩人）</span></li>
        <li><span class="name">島田 薫</span><span class="role">（小説家・緑陵大学教授）</span></li>
        <li><span class="name">●●●●</span><span class="role">（詩人）</span></li>
        <li><span class="name">●●●●</span><span class="role">（詩人）</span></li>
        <li><span class="name">岡部里香子</span><span class="role">（青い窓舎 代表取締役）</span></li>
        <li><span class="name">森川静江</span><span class="role">（青い窓舎 編集長）</span></li>
      </ul>
    </aside>

    <div class="publisher">
      <p class="tagline">アート＆ブックス</p>
      <div class="brand"><span class="dot"></span><span class="name">青い窓舎</span></div>
      <p>〒000-0000 みどり県青葉市若葉町1-2-3</p>
      <p class="contact-row">
        <svg viewBox="0 0 24 24" aria-hidden="true"><path fill="#2f74b5" d="M6.6 10.8a15 15 0 0 0 6.6 6.6l2.2-2.2c.3-.3.7-.4 1-.2 1.1.4 2.3.6 3.6.6.6 0 1 .4 1 1V20c0 .6-.4 1-1 1A17 17 0 0 1 3 4c0-.6.4-1 1-1h3.5c.6 0 1 .4 1 1 0 1.3.2 2.5.6 3.6.1.3 0 .7-.2 1z"/></svg>
        TEL 012-345-6789
      </p>
      <p class="contact-row">FAX 012-345-6790</p>
      <p>www.aoimadosha.example</p>
      <p>info@aoimadosha.example</p>
    </div>

    <p class="request">● 投稿規定・専用原稿用紙のご請求は、お電話またはメールにて青い窓舎までお気軽にどうぞ。</p>
  </section>
</main>
</body>
</html>
```